Bastion Electronic Security Web Site

We need a web site for our new company based in Sydney Australia.
We specialize in consulting supplying and installing electronic security systems. These include CCTV, Access control, Alarms, Intercom and Network cabling.
We pride our selves in giving our customers peace of mind giving back security and freedom to our customers. We pride in customer service quality products and expertise with and we do the job as though it is for our personal friends and family.
We need to be able to edit web site contents and update information.
Industry/Entity Type
Electronic

```html
<!DOCTYPE html>
<html lang="en">
<head>
<meta charset="utf-8">
<title>Bastion Electronic Security</title>
<link rel="stylesheet" href="https://fonts.googleapis.com/css2?family=Open+Sans:wght@400;600;700&display=swap">
<style>
:root{
  --blue:#1f4fb5;
  --blue-dark:#173c8e;
  --ink:#3a3a3a;
  --muted:#555;
  --page:#efefef;
  --band:#e4e4e4;
  --white:#fff;
  --footer:#2c2c2e;
  --line:#9a9a9a;
}
*{box-sizing:border-box;margin:0;padding:0}
html,body{width:851px;height:1200px;overflow:hidden}
body{position:relative;background:var(--page);font-family:"Open Sans",sans-serif;color:var(--ink)}
.abs{position:absolute}
.top-rule{left:0;top:0;width:851px;height:3px;background:var(--blue)}
.brand{left:70px;top:12px;color:var(--blue);line-height:1}
.brand-name{font-size:29px;font-weight:600;letter-spacing:-.5px}
.brand-sub{font-size:12px;color:var(--ink);margin-top:2px;border-top:2px solid var(--blue);padding-top:2px}
.call{left:627px;top:14px;display:flex;gap:8px;align-items:flex-start}
.call-text{line-height:1.05}
.call-label{font-size:17px;color:#444}
.call-number{font-size:19px;color:var(--blue)}
.nav{left:70px;top:63px;width:711px;height:26px;border-top:1px solid #cfcfcf;border-bottom:1px solid #cfcfcf;display:flex;align-items:center}
.nav a{font-size:9.5px;color:#333;text-decoration:none;padding:0 11px;height:100%;display:flex;align-items:center}
.nav a.active{background:var(--blue);color:var(--white);padding:0 13px;margin-right:2px}
.search{position:absolute;right:0;top:3px;width:168px;height:18px;background:var(--white);border:1px solid #d6d6d6;font-size:7px;padding:4px 4px;color:#444}
.search svg{position:absolute;right:4px;top:3px}
.hero{left:0;top:98px;width:851px;height:293px;background:linear-gradient(90deg,#7d7f82 0%,#a9abad 30%,#d4d6d8 55%,#9b9d9f 80%,#cfd1d3 100%)}
.hero-shade{left:0;top:98px;width:851px;height:293px;background:linear-gradient(90deg,rgba(40,40,40,.35),rgba(0,0,0,0) 55%)}
.hero-title{left:70px;top:211px;font-size:21px;font-weight:600;color:var(--white);line-height:1.25;letter-spacing:.2px}
.btn{background:linear-gradient(#2d63cf,var(--blue-dark));color:var(--white);font-size:8px;display:flex;align-items:center;justify-content:center;border-radius:2px;font-weight:600}
.hero-btn{left:70px;top:283px;width:75px;height:22px;font-weight:400}
.arrow{top:205px}
.welcome{left:0;top:391px;width:851px;height:73px;background:var(--band)}
.welcome-title{left:70px;top:404px;font-size:18px;color:#444;font-weight:400}
.welcome-title b{font-weight:600}
.welcome-text{left:70px;top:427px;width:482px;font-size:7.8px;color:var(--muted);line-height:1.35}
.brochure{left:625px;top:411px;width:156px;height:34px;font-size:9px;font-weight:400;box-shadow:0 1px 2px rgba(0,0,0,.4)}
.section-title{font-size:21px;color:var(--blue);font-weight:400}
.rule{height:0;border-top:1px dashed var(--line)}
.services-title{left:69px;top:490px}
.services-rule{left:70px;top:522px;width:711px}
.service{top:552px;width:130px;text-align:center}
.service-name{font-size:11px;color:#333}
.service-name.current{color:var(--blue)}
.service-disc{width:84px;height:84px;border-radius:50%;background:radial-gradient(circle at 50% 40%,#fff 60%,#e8e8e8);margin:12px auto 0;display:flex;align-items:center;justify-content:center;box-shadow:0 0 0 1px #e0e0e0,0 2px 4px rgba(0,0,0,.08)}
.service-disc.current{box-shadow:0 0 0 3px var(--blue)}
.service-floor{width:70px;height:6px;margin:8px auto 0;border-radius:50%;background:radial-gradient(rgba(0,0,0,.18),rgba(0,0,0,0) 70%)}
.service-text{font-size:8px;line-height:1.35;margin:10px auto 0;width:116px;color:#333}
.lower{left:0;top:751px;width:851px;height:343px;background:var(--band)}
.col-title{top:770px}
.col-rule{top:800px;width:229px}
.about-photo{left:71px;top:811px;width:223px;height:124px;background:linear-gradient(135deg,#5a5c60,#9fa2a6 45%,#cfd1d4 60%,#6d6f73)}
.about-text{left:71px;top:950px;width:220px;font-size:6.8px;line-height:1.4;color:#444}
.about-text p+p{margin-top:8px}
.quotes{left:317px;top:811px;width:210px;font-size:7.9px;line-height:1.35;color:#333}
.quote+.quote{margin-top:20px}
.quote cite{font-style:normal;font-size:10px;font-weight:600;color:#333;margin-left:4px}
.divider{top:805px;width:1px;height:235px;background:#d4d4d4}
.field{left:570px;width:211px;height:23px;background:#f6f6f6;border:1px solid #e2e2e2;font-size:7px;color:#888;padding:6px 9px}
.read{width:80px;height:25px;font-size:8px}
.footer{left:0;top:1094px;width:851px;height:106px;background:var(--footer);border-top:5px solid var(--blue)}
.foot-links{left:72px;top:1115px;font-size:7.5px;color:var(--white);display:flex;gap:10px}
.contacts-h{left:74px;top:1134px;font-size:15px;color:var(--white)}
.contacts{left:75px;top:1159px;font-size:8.5px;color:var(--white);line-height:1.6;font-weight:600}
.social-h{left:351px;top:1109px;font-size:15px;color:var(--white)}
.social{left:354px;top:1134px;display:flex;gap:12px}
.social span{width:14px;height:14px;border-radius:50%;background:#dcdcdc}
.foot-brand{left:665px;top:1110px;color:var(--white);text-align:center;line-height:1}
.foot-brand .brand-name{font-size:25px}
.foot-brand .brand-sub{color:var(--white);border-top-color:var(--white);font-size:11px}
.rights{right:66px;top:1172px;font-size:6.5px;color:var(--white)}
</style>
</head>
<body>
<div class="abs top-rule"></div>

<header>
  <div class="abs brand">
    <div class="brand-name">Bastion</div>
    <div class="brand-sub">Electronic Security</div>
  </div>
  <div class="abs call">
    <svg width="40" height="38" viewBox="0 0 40 38" aria-hidden="true">
      <path d="M4 10c0-5 7-8 16-8s16 3 16 8v3h-8v-3c-2-1-5-2-8-2s-6 1-8 2v3H4z" fill="#4a4a4a"/>
      <path d="M8 15h24l5 17H3z" fill="#4a4a4a"/>
      <circle cx="20" cy="24" r="5" fill="#efefef"/>
      <circle cx="20" cy="24" r="2" fill="#4a4a4a"/>
    </svg>
    <div class="call-text">
      <div class="call-label">Call Now !</div>
      <div class="call-number">012 3456 7890</div>
    </div>
  </div>
  <nav class="abs nav">
    <a class="active" href="#">Home</a>
    <a href="#">About Us</a>
    <a href="#">Services</a>
    <a href="#">Products</a>
    <a href="#">News</a>
    <a href="#">Contact Us</a>
    <div class="search">Search . . .
      <svg width="11" height="11" viewBox="0 0 11 11" aria-hidden="true"><circle cx="4.5" cy="4.5" r="3.3" fill="none" stroke="#aaa" stroke-width="1.3"/><path d="M7 7l3 3" stroke="#aaa" stroke-width="1.5"/></svg>
    </div>
  </nav>
</header>

<section>
  <div class="abs hero" role="img" aria-label="Close-up photograph of white security surveillance cameras"></div>
  <div class="abs hero-shade"></div>
  <h1 class="abs hero-title">SECURITY SERVICES AND<br>MANAGEMENT AT FAIR PRICES</h1>
  <div class="abs btn hero-btn">Learn more</div>
  <svg class="abs arrow" style="left:8px" width="36" height="52" viewBox="0 0 36 52" aria-hidden="true"><path d="M32 2L4 26l28 24" fill="none" stroke="#fff" stroke-width="3"/></svg>
  <svg class="abs arrow" style="left:808px" width="36" height="52" viewBox="0 0 36 52" aria-hidden="true"><path d="M4 2l28 24L4 50" fill="none" stroke="#fff" stroke-width="3"/></svg>
</section>

<section>
  <div class="abs welcome"></div>
  <h2 class="abs welcome-title">Welcome to <b>Bastion Electronic Security</b></h2>
  <p class="abs welcome-text">Lorem Ipsum is simply dummy text of the printing and typesetting industry. Lorem Ipsum has been the industry's standard dummy text ever since the 1500s . . .</p>
  <div class="abs btn brochure">DOWNLOAD BROCHURE</div>
</section>

<section>
  <h2 class="abs section-title services-title">SERVICES</h2>
  <div class="abs rule services-rule"></div>

  <div class="abs service" style="left:63px">
    <div class="service-name current">CCTV</div>
    <div class="service-disc current">
      <svg width="48" height="30" viewBox="0 0 48 30" aria-hidden="true"><path d="M2 8l30-7 3 8-30 8z" fill="#222"/><path d="M6 16l3 6" stroke="#222" stroke-width="3"/><path d="M26 14v7h10v-3h6v10h-4v-4h-2" fill="none" stroke="#222" stroke-width="3"/></svg>
    </div>
    <div class="service-floor"></div>
    <p class="service-text">Lorem Ipsum is simply dummy text of the printing and typesetting industry.</p>
  </div>

  <div class="abs service" style="left:210px">
    <div class="service-name">Access control</div>
    <div class="service-disc">
      <svg width="36" height="40" viewBox="0 0 36 40" aria-hidden="true"><rect x="2" y="2" width="32" height="36" fill="none" stroke="#222" stroke-width="3"/><path d="M12 18v-5a6 6 0 0112 0v5" fill="none" stroke="#222" stroke-width="3"/><rect x="9" y="18" width="18" height="14" rx="2" fill="#222"/><circle cx="18" cy="25" r="2" fill="#fff"/></svg>
    </div>
    <div class="service-floor"></div>
    <p class="service-text">Lorem Ipsum is simply dummy text of the printing and typesetting industry.</p>
  </div>

  <div class="abs service" style="left:358px">
    <div class="service-name">Alarms</div>
    <div class="service-disc">
      <svg width="40" height="36" viewBox="0 0 40 36" aria-hidden="true"><path d="M11 30v-12a9 9 0 0118 0v12z" fill="#222"/><rect x="7" y="30" width="26" height="5" fill="#222"/><path d="M20 2v5M6 8l4 4M34 8l-4 4M1 20h5M34 20h5" stroke="#222" stroke-width="2.5"/></svg>
    </div>
    <div class="service-floor"></div>
    <p class="service-text">Lorem Ipsum is simply dummy text of the printing and typesetting industry.</p>
  </div>

  <div class="abs service" style="left:508px">
    <div class="service-name">Intercom</div>
    <div class="service-disc">
      <svg width="40" height="40" viewBox="0 0 40 40" aria-hidden="true"><path d="M8 4l6 8-4 4c2 5 7 10 12 12l4-4 8 6-4 6C18 36 4 22 2 10z" fill="#222"/><path d="M22 10a8 8 0 018 8M22 4a14 14 0 0114 14" fill="none" stroke="#222" stroke-width="2.5"/></svg>
    </div>
    <div class="service-floor"></div>
    <p class="service-text">Lorem Ipsum is simply dummy text of the printing and typesetting industry.</p>
  </div>

  <div class="abs service" style="left:656px">
    <div class="service-name">Network cabling</div>
    <div class="service-disc">
      <svg width="34" height="44" viewBox="0 0 34 44" aria-hidden="true"><rect x="20" y="2" width="10" height="8" fill="#222"/><path d="M25 10v6c0 5-10 4-10 11s8 6 8 11c0 3-5 4-12 4" fill="none" stroke="#222" stroke-width="3.5"/></svg>
    </div>
    <div class="service-floor"></div>
    <p class="service-text">Lorem Ipsum is simply dummy text of the printing and typesetting industry.</p>
  </div>
</section>

<section>
  <div class="abs lower"></div>

  <h2 class="abs section-title col-title" style="left:71px">About Us</h2>
  <div class="abs rule col-rule" style="left:71px"></div>
  <div class="abs about-photo" role="img" aria-label="Photograph of a businessman holding a glowing digital padlock"></div>
  <div class="abs about-text">
    <p>Time is one of the most precious commodities people have, yet in today's fast paced, "doing more with less" world, it can be a struggle to have enough of it to accomplish our daily responsibilities and pursue our passions.</p>
    <p>Harbourside Helpers can help! We are the area's first concierge service that will help you with your to do list, running errands, become your personal assistant, anything to make your life easy and to maximize the value of time.</p>
  </div>
  <div class="abs btn read" style="left:71px;top:1042px">READ MORE</div>

  <div class="abs divider" style="left:308px"></div>

  <h2 class="abs section-title col-title" style="left:317px">Testimonials</h2>
  <div class="abs rule col-rule" style="left:317px"></div>
  <div class="abs quotes">
    <p class="quote">“ Aenean placerat nunc lorem, vitae suscipit mi luctus quis. In ligula lorem, ultricies volutpat arcu et, ultrices cursus enim.Aenean placerat nunc lorem, vitae suscipit mi luctus quis. In ligula lorem, ultricies volutpat arcu et, ultrices cursus enim. ” <cite>Peter Walsh</cite></p>
    <p class="quote">“ Aenean placerat nunc lorem, vitae suscipit mi luctus quis. In ligula lorem, ultricies volutpat arcu et, ultrices cursus enim.Aenean placerat nunc lorem, vitae suscipit mi luctus quis. In ligula lorem, ultricies volutpat arcu et, ultrices cursus enim. ” <cite>Mr. Kenji</cite></p>
    <p class="quote">“ Aenean placerat nunc lorem, vitae suscipit mi luctus quis. In ligula lorem, ultricies volutpat arcu et, ultrices cursus enim.Aenean placerat nunc lorem, vitae suscipit mi luctus quis. In ligula lorem, ultricies volutpat arcu et, ultrices cursus enim. ” <cite>Mrs. Carla Reed</cite></p>
  </div>
  <div class="abs btn read" style="left:318px;top:1042px">READ MORE</div>

  <div class="abs divider" style="left:554px"></div>

  <h2 class="abs section-title col-title" style="left:559px">Quick Contact</h2>
  <div class="abs rule col-rule" style="left:560px;width:229px"></div>
  <div class="abs field" style="top:813px">Name</div>
  <div class="abs field" style="top:845px">Email</div>
  <div class="abs field" style="top:876px">Phone Number</div>
  <div class="abs field" style="top:907px;height:104px">Message</div>
  <div class="abs btn read" style="left:718px;top:1042px;width:65px">SUBSCRIBE</div>
</section>

<footer>
  <div class="abs footer"></div>
  <div class="abs foot-links"><span>|</span><span>Home</span><span>|</span><span>Services</span><span>|</span><span>Blog</span><span>|</span><span>Rates</span><span>|</span><span>Contact Us</span><span>|</span></div>
  <div class="abs contacts-h">Contacts:</div>
  <div class="abs contacts">Phone: (+61) 02 555 0101<br>Mobile: (+61) 02 555 0102</div>
  <div class="abs social-h">Social Icons:</div>
  <div class="abs social"><span></span><span></span><span></span><span></span><span></span></div>
  <div class="abs foot-brand">
    <div class="brand-name">Bastion</div>
    <div class="brand-sub">Electronic Security</div>
  </div>
  <div class="abs rights">All Rights Reserved</div>
</footer>
</body>
</html>
```